Figure for Manufacture of Wound Healing Gel

Who we are: We are a nationally funded bioengineering laboratory at Harwell Crest University conducting research on the tendon healing properties of a gel manufactured from real tendon.

What we need: We require a figure piece that will be included in an academic publication. With that in mind, the figure must be professional, clear, and concise. A reader would need to glance at the figure for only a moment to understand the process of how we manufacture and store tendon gel. Actual pictures of the in-between steps are included and will need to be cropped to improve the professional look of the design.

The Details: The figure should stepwise show the process of how we manufacture and store tendon gel. In brief, we harvest tendon from donor cadavers. Those tendons undergo decellularization, lyophilization (fancy word for freeze-drying), and are milled into a fine powder. The powder is set in acidified water and treated with digestive enzymes. After 24 hrs, the gel is brought to physiologic pH and salinity and placed in vials. The vials are frozen and again lyophilized (this is so they can be stored and transported easily). Finally the samples are reconstituted with DI water.

The Figure: Should be a linear process (horizontal). The following are the actual steps we wish to include (steps need not be numbered necessarily as long as they are in logical order...

1.) A picture of harvested tendon (Step 1.jpg)
2.) Written description: "Decellularization, lyophilization, and milling"
3.) A picture of milled tendon powder (Step 2.jpg)
4.) Written description: "Digestion with pepsin before establishing physiologic pH and salinity".
5.) A picture of gel (Step 3.jpg)
6.) Written description: "Lyophilization of aliquots"
7.) A picture of freeze-dried gel (Step 4.jpg)
8.) Written description: "Reconstitution with DI water"
9.) A picture of reconstituted gel (Step 5.jpg)

Feel free to message for any questions, comments, or clarifications.

```html
<!DOCTYPE html>
<html lang="en">
<head>
<meta charset="utf-8">
<title>Manufacture and storage of Tendon Gel</title>
<link rel="stylesheet" href="https://fonts.googleapis.com/css2?family=Open+Sans:wght@400;600;700;800&display=swap">
<style>
  :root {
    --navy: #0a2150;
    --ink: #0b0b0b;
    --white: #ffffff;
    --paper: #ffffff;
    --font: "Open Sans", Arial, sans-serif;
  }
  * { box-sizing: border-box; margin: 0; padding: 0; }
  html, body { width: 1200px; height: 1000px; overflow: hidden; background: var(--paper); }
  .figure { position: relative; width: 1200px; height: 1000px; font-family: var(--font); color: var(--ink); }
  .figure-title { position: absolute; left: 80px; top: 57px; font-size: 31px; font-weight: 700; letter-spacing: -0.2px; line-height: 1.2; }
  .section-title { position: absolute; left: 83px; font-size: 20.5px; font-weight: 400; color: var(--navy); line-height: 1.2; }
  .section-title.manufacturing { top: 108px; }
  .section-title.storage { top: 338px; left: 80px; }
  .shapes { position: absolute; left: 0; top: 0; }
  .step-number { position: absolute; font-size: 50px; font-weight: 800; line-height: 1; color: var(--ink); }
  .step-text { position: absolute; text-align: center; font-size: 12.5px; line-height: 17.5px; color: var(--ink); }
  .photo { position: absolute; }
  .caption { position: absolute; font-size: 11px; line-height: 15px; color: var(--white); }
  .photo-tendon { left: 214px; top: 149px; width: 171px; height: 131px; background: radial-gradient(ellipse at 50% 55%, #d9cdb4 0%, #bdb6aa 45%, #8f8c87 100%); }
  .photo-powder { left: 590px; top: 149px; width: 171px; height: 131px; background: radial-gradient(ellipse at 50% 45%, #eee4cf 0%, #b9b6b0 45%, #85827e 100%); }
  .photo-gel { left: 963px; top: 149px; width: 172px; height: 131px; background: radial-gradient(ellipse at 45% 50%, #f3f3f0 0%, #a9a8a6 45%, #6e6d6b 100%); }
  .photo-lyophilised { left: 209px; top: 379px; width: 181px; height: 238px; background: linear-gradient(180deg, #8d8a86 0%, #5e5b58 35%, #3d3b3a 60%, #d9d1c0 78%, #2f2e2d 100%); }
  .photo-reconstituted { left: 587px; top: 377px; width: 183px; height: 240px; background: linear-gradient(180deg, #8f8b86 0%, #5f5c59 35%, #3c3a39 60%, #e1dccd 78%, #2d2c2b 100%); }
</style>
</head>
<body>
<main class="figure">
  <h1 class="figure-title">Manufacture and storage of Tendon Gel</h1>
  <h2 class="section-title manufacturing">Manufacturing process</h2>
  <h2 class="section-title storage">Storage of Tendon Gel</h2>

  <svg class="shapes" width="1200" height="1000" viewBox="0 0 1200 1000" aria-hidden="true">
    <g fill="var(--navy)">
      <path d="M122,140 H398 C410,168 428,190 450,204 L452,316 H122 Z"/>
      <path d="M498,140 H776 C788,168 806,190 828,204 L830,316 H498 Z"/>
      <path d="M872,140 H1145 V316 H872 Z"/>
      <path d="M126,368 H378 C392,400 410,428 440,448 L470,540 C440,575 418,610 404,644 H126 Z"/>
      <path d="M504,368 H783 V644 H410 C423,610 445,578 476,544 L504,510 Z"/>
    </g>
    <g fill="var(--white)" stroke="var(--navy)" stroke-width="1.2">
      <circle cx="119" cy="229" r="61"/>
      <circle cx="485" cy="231" r="56"/>
      <circle cx="859" cy="229" r="58"/>
      <circle cx="121" cy="482" r="66"/>
      <circle cx="495" cy="480" r="56"/>
    </g>
  </svg>

  <span class="step-number" style="left:80px;top:146px;">1</span>
  <span class="step-number" style="left:457px;top:148px;">2</span>
  <span class="step-number" style="left:831px;top:144px;">3</span>
  <span class="step-number" style="left:84px;top:400px;">4</span>
  <span class="step-number" style="left:466px;top:398px;">5</span>

  <p class="step-text" style="left:64px;top:202px;width:112px;">Harvesting of Tendons from cadaver sources</p>
  <p class="step-text" style="left:430px;top:204px;width:112px;">Decellularization, lyophilization, and milling</p>
  <p class="step-text" style="left:806px;top:186px;width:106px;">Digestion with pepsin before establishing physiologic pH and salinity</p>
  <p class="step-text" style="left:68px;top:461px;width:110px;">Lyophilization of aliquots</p>
  <p class="step-text" style="left:445px;top:462px;width:100px;">Reconstitution with DI water</p>

  <div class="photo photo-tendon" role="img" aria-label="Photo of harvested tendons in a glass dish"></div>
  <div class="photo photo-powder" role="img" aria-label="Photo of milled tendon powder in a glass dish"></div>
  <div class="photo photo-gel" role="img" aria-label="Photo of digested tendon gel in a glass dish"></div>
  <div class="photo photo-lyophilised" role="img" aria-label="Photo of a vial with lyophilised gel sample"></div>
  <div class="photo photo-reconstituted" role="img" aria-label="Photo of a vial with reconstituted gel sample"></div>

  <p class="caption" style="left:214px;top:281px;">Fig. 1: Harvested Tendon</p>
  <p class="caption" style="left:590px;top:281px;">Fig. 2: Milled Tendon powder</p>
  <p class="caption" style="left:963px;top:281px;width:180px;">Fig. 3: Digested sample at physiological pH and salinity</p>
  <p class="caption" style="left:210px;top:620px;">Fig. 4: Lyophilised sample</p>
  <p class="caption" style="left:588px;top:620px;">Fig. 5: Reconstituted sample</p>
</main>
</body>
</html>
```